Re-Design of existing Storeloom Website

Hi,

We are looking for a skilled person to work with us on improving the design of our website to make it more user friendly. We are a Makeup brush and makeup accessories company and our current website can be viewed at pillowandfern dot com.We are looking to simplify the layout and make it more modern and mobile friendly.

We have designs in mind which we would like to implement to our site which we feel would work better for us to increase traffic and sales.

We would like the layout to have clear sections for brushes,lashes ,sponge and also our tutorials on the landing page.

Industry/Entity Type

Hair And Beauty

Number of Pages Required

5+ page

Font styles to use
Sans Serif

Colors
b8a6cd
d3a5cc
eea4c8
ffffff
000000

Requirements
Must have
• -Clear ,modern landing page.
• -easy navigation
• -simple design
• -professional design approach
Nice to have
• cross selling pop up
Should not have
• over use of bold colour.

```html
<!DOCTYPE html>
<html lang="en">
<head>
<meta charset="utf-8">
<title>Pillow&amp;Fern — Makeup Brushes &amp; Lashes</title>
<link rel="stylesheet" href="https://fonts.googleapis.com/css2?family=Titillium+Web:wght@200;300;400&display=swap">
<style>
  :root {
    --black: #000000;
    --white: #ffffff;
    --pink: #d57aa9;
    --pink-soft: #eea4c8;
    --mauve: #b96a98;
    --grey-dark: #4f4f4f;
    --grey-mid: #9e9e9e;
    --grey-text: #9a9a9a;
    --footer-text: #a8a8a8;
  }
  * { margin: 0; padding: 0; box-sizing: border-box; }
  html, body { width: 1200px; height: 1200px; overflow: hidden; background: var(--black); }
  body { font-family: "Titillium Web", Arial, sans-serif; color: var(--white); position: relative; }

  .hero { position: absolute; left: 0; top: 0; width: 1200px; height: 712px; background: var(--black); overflow: hidden; }
  .hero-photo {
    position: absolute; left: 0; top: 0; width: 820px; height: 712px;
    background:
      radial-gradient(ellipse 55% 60% at 38% 45%, #e6cfc4 0%, #c9b3a8 45%, rgba(0,0,0,0) 100%),
      linear-gradient(90deg, #efe9e2 0%, #d8d0c8 35%, #7a7570 62%, #000 100%);
  }
  .brand {
    position: absolute; left: 745px; top: 270px;
    font-weight: 200; font-size: 60px; letter-spacing: -1px; line-height: 1;
    color: var(--pink);
  }
  .main-nav { position: absolute; left: 835px; top: 404px; list-style: none; }
  .main-nav li { font-size: 14px; font-weight: 300; height: 30.2px; line-height: 18px; letter-spacing: 0.2px; }
  .main-nav .has-sub::after {
    content: ""; display: inline-block; margin-left: 12px; vertical-align: 1px;
    border-left: 4.5px solid transparent; border-right: 4.5px solid transparent; border-top: 8px solid var(--pink);
  }

  .tile { position: absolute; width: 600px; height: 188px; overflow: hidden; }
  .tile-title { position: absolute; font-weight: 300; font-size: 39px; line-height: 1; letter-spacing: -0.5px; }

  .tile-products { left: 0; top: 712px; background: var(--white); }
  .tile-products .product-photo {
    position: absolute; left: 400px; top: 0; width: 140px; height: 188px;
    background: linear-gradient(90deg, #f3d7e6 0%, #d8559d 30%, #f1cde0 50%, #c8438b 75%, #f4dcea 100%);
    opacity: 0.55;
  }
  .tile-products .tile-title { left: 37px; top: 120px; color: var(--grey-text); }

  .tile-tutorials { left: 600px; top: 712px; background: linear-gradient(100deg, #b8719d 0%, #c07fa6 55%, #cf8fb2 100%); }
  .tile-tutorials .tile-title { left: 51px; top: 120px; color: var(--white); }

  .tile-social { left: 0; top: 900px; background: linear-gradient(160deg, #5a5a5a 0%, #484848 60%, #3d3d3d 100%); }
  .social-mark { position: absolute; left: 33px; top: 114px; width: 38px; height: 38px; border: 3px solid var(--white); border-radius: 9px; }
  .social-kicker { position: absolute; left: 91px; top: 93px; font-size: 20px; font-weight: 300; line-height: 1; }
  .social-name { position: absolute; left: 89px; top: 112px; font-size: 41px; font-weight: 300; line-height: 1; }

  .tile-newsletter { left: 600px; top: 900px; background: var(--grey-mid); }
  .news-kicker { position: absolute; left: 38px; top: 86px; font-size: 19px; font-weight: 300; line-height: 1; }
  .news-title { position: absolute; left: 36px; top: 104px; font-size: 41px; font-weight: 300; line-height: 1; }
  .news-note { position: absolute; left: 36px; top: 150px; font-size: 11px; font-weight: 300; }
  .news-field { position: absolute; left: 305px; top: 95px; width: 263px; height: 59px; background: var(--white); border-radius: 4px; }
  .news-field svg { position: absolute; right: 20px; top: 20px; }

  .site-footer { position: absolute; left: 0; top: 1087px; width: 1200px; height: 113px; background: var(--black); }
  .footer-links { position: absolute; left: 33px; top: 52px; font-size: 12px; font-weight: 300; color: var(--footer-text); }
  .footer-copy { position: absolute; right: 38px; top: 52px; font-size: 12px; font-weight: 300; color: var(--footer-text); }
</style>
</head>
<body>
  <header class="hero">
    <div class="hero-photo" role="img" aria-label="Portrait of a smiling model with red lipstick and a white fur hood"></div>
    <div class="brand">Pillow&amp;Fern</div>
    <ul class="main-nav">
      <li>LUXURY SILK LASHES</li>
      <li>DELUXE LASHES</li>
      <li>INDIVIDUAL BRUSHES</li>
      <li>BRUSH SETS</li>
      <li>CLEARANCE</li>
      <li class="has-sub">TUTORIALS</li>
      <li class="has-sub">DEWBLUR SPONGE</li>
    </ul>
  </header>

  <section class="tile tile-products">
    <div class="product-photo" role="img" aria-label="Four pink-handled makeup brushes"></div>
    <h2 class="tile-title">NEW PRODUCTS</h2>
  </section>

  <section class="tile tile-tutorials" role="img" aria-label="Hand holding an eyeshadow palette in a pink tint">
    <h2 class="tile-title">MAKE UP TUTORIALS</h2>
  </section>

  <section class="tile tile-social" role="img" aria-label="Makeup brushes, mascara wand and eyelash curler on a grey surface">
    <div class="social-mark"></div>
    <div class="social-kicker">FOLLOW US ON</div>
    <div class="social-name">SNAPFEED</div>
  </section>

  <section class="tile tile-newsletter">
    <div class="news-kicker">SUBSCRIBE TO OUR</div>
    <div class="news-title">NEWSLETTER</div>
    <div class="news-note">Be the first to know about new products and sales</div>
    <div class="news-field">
      <svg width="20" height="18" viewBox="0 0 20 18" aria-hidden="true">
        <path d="M0 8 L20 0 L15 18 L9 12 Z" fill="#c76aa0"/>
        <path d="M9 12 L20 0 L7 10 L7 17 Z" fill="#a9508a"/>
      </svg>
    </div>
  </section>

  <footer class="site-footer">
    <div class="footer-links">Luxury Silk Lashes | Deluxe Lashes | Individual Brushes | Brush Sets | Clearance | Tutorials | Dewblur Sponge</div>
    <div class="footer-copy">© 2018, Pillow&amp;Fern. Powered by Storeloom</div>
  </footer>
</body>
</html>
```